Copperleaf Motorized Shade Business Card

Hello, we've had our logo made. Now we are looking for a clean and cool looking business card. One side can just be the logo with any design elements that might look good with it. The other side will be Name, Phone Number and Email. There will not be an address on the card.

```html
<!DOCTYPE html>
<html lang="en">
<head>
<meta charset="utf-8">
<title>Copperleaf Motorized Shade – Business Card</title>
<link rel="stylesheet" href="https://fonts.googleapis.com/css2?family=Montserrat:wght@400;500;600;700&display=swap">
<style>
  :root {
    --navy: #0d3a70;
    --sun: #fdbd16;
    --white: #ffffff;
    --edge: #5a5a5a;
    --sheet: #ffffff;
  }
  * { margin: 0; padding: 0; box-sizing: border-box; }
  html, body { width: 957px; height: 1200px; overflow: hidden; background: var(--sheet); }
  .sheet {
    position: relative;
    width: 957px;
    height: 1200px;
    border: 3px solid var(--sun);
    font-family: "Montserrat", sans-serif;
  }
  .card {
    position: absolute;
    left: 46px;
    width: 863px;
    height: 520px;
    overflow: hidden;
  }
  .card--front { top: 55px; background: var(--white); border: 2px solid var(--edge); }
  .card--back { top: 626px; background: var(--navy); }
  .card__waves { position: absolute; left: 0; top: 0; width: 100%; height: 100%; }
  .brand {
    position: absolute;
    left: 0; right: 0;
    display: flex;
    justify-content: center;
    align-items: center;
    gap: 14px;
  }
  .card--front .brand { top: 206px; }
  .card--back .brand { top: 222px; }
  .brand__mark { width: 26px; height: 26px; background: var(--sun); }
  .brand__name { font-size: 34px; font-weight: 700; letter-spacing: 0.5px; white-space: nowrap; }
  .card--front .brand__name { color: var(--navy); }
  .card--back .brand__name { color: var(--white); }
  .contact-name {
    position: absolute;
    left: 59px; top: 413px;
    color: var(--white);
    font-size: 28px; font-weight: 600;
    letter-spacing: 0.5px;
    white-space: nowrap;
  }
  .contact-details {
    position: absolute;
    right: 59px; top: 392px;
    text-align: right;
    color: var(--white);
    white-space: nowrap;
  }
  .contact-details__phone { font-size: 27px; font-weight: 500; line-height: 36px; }
  .contact-details__email { font-size: 22px; font-weight: 400; line-height: 40px; }
</style>
</head>
<body>
<div class="sheet">
  <section class="card card--front">
    <svg class="card__waves" viewBox="0 0 863 520" preserveAspectRatio="none" aria-hidden="true">
      <path d="M0 289 Q431.5 455 863 289 V520 H0 Z" fill="var(--sun)"/>
      <path d="M0 330 Q431.5 422 863 330 V520 H0 Z" fill="var(--navy)"/>
    </svg>
    <div class="brand">
      <span class="brand__mark"></span>
      <span class="brand__name">Copperleaf Motorized Shade</span>
    </div>
    <p class="contact-name">RILEY MARSH</p>
    <div class="contact-details">
      <p class="contact-details__phone">098 765 4321</p>
      <p class="contact-details__email">riley@copperleaf.com</p>
    </div>
  </section>

  <section class="card card--back">
    <div class="brand">
      <span class="brand__mark"></span>
      <span class="brand__name">Copperleaf Motorized Shade</span>
    </div>
  </section>
</div>
</body>
</html>
```